Ridgeline E-Bike Tours NZ

We are an Electric Mountain bike tour company in New Zealand. We will be offering bike rental and guided tours around the Nelson region in New Zealand. I want our website to represent both Mountain biking and New Zealand with the colours layout and features. We want tabs for the following:
-1 about us
-2 what we offer
-3 bookings/contact
Under the about us tab will be who we are as a a company. I want the ability to add videos to each of these tabs as we move foward with videos of the tracks we will be riding. I want the website to be editable so I can add and remove videos/photos myself. Also "our bikes" will be under this tab.
Under the what we offer tab will be
-1 bike rental and pricing
-2 guided tours and pricing
-3 recommended package deals.
I want to able to put the tracks under the guided tours tab and select beginner/ intermediate/advanced and have the tracks in each of the following to match the rider level. Also to be able to have a small video of the track would be great in this section.
Bookings and contact tab
(Further information for this tab to be updated soon)
Coded - Design and coding required
1 page
- Silver ferns, kiwi, mountains

```html
<!DOCTYPE html>
<html lang="en">
<head>
<meta charset="utf-8">
<title>Ridgeline E-Bike Tours NZ</title>
<link href="https://fonts.googleapis.com/css2?family=Oswald:wght@500;600&family=Roboto:wght@400;500;700&display=swap" rel="stylesheet">
<style>
:root{
  --navy:#1f2137;
  --navy-deep:#15172a;
  --orange:#f47b0b;
  --ink:#111;
  --text:#444;
  --paper:#fff;
  --mist:#f4f2f2;
  --line:#c9c9c9;
}
*{margin:0;padding:0;box-sizing:border-box}
html,body{width:1200px;height:2889px;overflow:hidden}
body{position:relative;font-family:'Roboto',sans-serif;color:var(--text);background:var(--paper)}
.abs{position:absolute}
h2{font-family:'Oswald',sans-serif;font-weight:600;color:var(--ink);font-size:32px;letter-spacing:.5px}
.white{color:#fff}

/* header */
.header{left:0;top:0;width:1200px;height:150px;background:var(--navy)}
.topbar{left:0;top:0;width:1200px;height:40px;border-bottom:1px solid #34364e}
.welcome{left:173px;top:12px;font-size:12px;color:#fff}
.social{display:flex;gap:10px}
.social span{width:26px;height:26px;border:1.5px solid #fff;border-radius:50%;display:block}
.header-info{font-size:15px;color:#fff;line-height:20px}
.header-info small{font-size:14px;color:#ddd}
.logo{left:522px;top:5px;width:154px;height:154px;border-radius:50%;background:#fff;border:5px solid var(--navy);display:flex;align-items:center;justify-content:center;z-index:3}
.logo span{font-family:'Oswald',sans-serif;font-weight:600;font-size:27px;color:var(--navy)}
.navbar{left:0;top:145px;width:1200px;z-index:2}
.nav{left:0;top:172px;width:1200px;display:flex;justify-content:center;gap:56px;z-index:3;font-size:14px;font-weight:700;color:#fff}

/* hero */
.hero{left:0;top:160px;width:1200px;height:549px;background:linear-gradient(180deg,#233452 0%,#3e5a6e 30%,#6a6a3c 62%,#2d2a1a 100%)}
.book{left:173px;top:227px;width:353px;height:413px;background:rgba(12,12,16,.82);text-align:center;color:#fff}
.book h3{font-family:'Oswald',sans-serif;font-weight:600;font-size:30px;margin-top:20px}
.book .rule{width:54px;height:3px;background:#fff;margin:8px auto 0}
.book .post{margin:30px auto 0;width:297px;height:42px;border:1.5px solid #fff;border-radius:21px;font-size:12px;line-height:39px}
.book .ret{margin-top:20px;font-size:12px}
.dates{display:flex;justify-content:center;gap:40px;margin-top:20px;text-align:left}
.dates .lbl{font-size:13px}
.dates .day{display:flex;align-items:center;gap:10px;margin-top:16px}
.dates .day b{font-family:'Oswald',sans-serif;font-size:32px;font-weight:600}
.dates .day i{font-style:normal;font-size:14px;line-height:19px}
.dates .time{font-size:13px;margin-top:18px;display:flex;align-items:center;gap:8px}
.btn{display:inline-block;background:var(--orange);color:#fff;border-radius:20px;font-size:14px;font-weight:700;text-align:center}
.book .btn{margin-top:34px;width:125px;height:36px;line-height:36px}

/* about */
.title-line{height:3px;background:var(--orange)}
.about-copy{left:173px;top:825px;width:440px;font-size:11.5px;line-height:19.3px;text-align:justify;color:#555}
.btn-dark{left:173px;top:1061px;width:146px;height:37px;line-height:37px;border-radius:19px;background:var(--ink);color:#fff;font-size:13px;font-weight:700;text-align:center}
.video-frame{left:755px;top:788px;width:270px;height:310px;border:3px solid var(--line)}
.video-tag{left:977px;top:955px;transform:rotate(-90deg);font-family:'Oswald',sans-serif;font-size:22px;color:#bdbdbd;letter-spacing:2px}
.video-photo{left:684px;top:770px;width:293px;height:293px;background:linear-gradient(180deg,#7a8fa0 0%,#2f4f72 45%,#384a3c 75%,#1e2418 100%)}
.play{left:50%;top:50%;transform:translate(-50%,-50%);width:40px;height:40px;border-radius:50%;background:rgba(255,255,255,.45)}
.play::after{content:"";position:absolute;left:15px;top:11px;border-left:14px solid #fff;border-top:9px solid transparent;border-bottom:9px solid transparent}

/* offer */
.offer{left:0;top:1198px;width:1200px;height:597px;background:linear-gradient(180deg,#1e221d 0%,#141712 100%)}
.offer-lead{left:270px;top:1327px;width:660px;text-align:center;font-size:12px;line-height:21px;color:#fff;font-weight:500}
.card{width:270px;text-align:center}
.card .ph{height:189px}
.card h4{margin-top:22px;font-size:13px;color:var(--orange);font-weight:700}
.card p{margin-top:10px;font-size:11px;line-height:16px;color:#fff;padding:0 6px}
.card .btn{margin-top:26px;width:102px;height:31px;line-height:31px;font-size:11px}

/* video */
.videos{left:0;top:1795px;width:1200px;height:347px;background:var(--mist)}
.thumb{width:197px}
.thumb .ph{position:relative;height:140px;background:linear-gradient(180deg,#4e6379 0%,#c6cbc6 28%,#4d5a4c 42%,#22301f 100%)}
.thumb p{margin-top:20px;font-size:13px;font-weight:500;color:var(--ink)}
.arrow{width:27px;height:27px;background:var(--orange)}

/* contact */
.field{height:36px;border:1px solid #ccc;font-size:11.5px;color:#777;padding:10px 12px}

/* footer */
.footer{left:0;top:2591px;width:1200px;height:242px;background:var(--navy)}
.bottom{left:0;top:2833px;width:1200px;height:56px;background:var(--navy-deep);font-size:11px;color:#ccc;padding:20px 0 0 173px}
.f-h{font-size:15px;font-weight:700;color:#fff}
.f-txt{font-size:11px;line-height:17px;color:#ddd}
.f-list li{list-style:none;font-size:11px;color:#ddd;margin-bottom:11px;display:flex;align-items:center;gap:10px}
.f-list li::before{content:"";border-left:5px solid #fff;border-top:4px solid transparent;border-bottom:4px solid transparent}
</style>
</head>
<body>

<!-- hero background -->
<div class="abs hero" role="img" aria-label="Photo of an orange electric mountain bike parked on a hilltop above a valley at dusk"></div>

<!-- header -->
<div class="abs header"></div>
<div class="abs topbar"></div>
<div class="abs welcome">Welcome to Ridgeline E-Bike Tours NZ</div>
<div class="abs social" style="left:890px;top:6px"><span></span><span></span><span></span><span></span></div>

<svg class="abs" style="left:170px;top:62px" width="18" height="26" viewBox="0 0 18 26"><path d="M9 0C4 0 0 4 0 9c0 7 9 17 9 17s9-10 9-17c0-5-4-9-9-9z" fill="#f47b0b"/><circle cx="9" cy="9" r="3.5" fill="#1f2137"/></svg>
<div class="abs header-info" style="left:204px;top:62px">14 Kowhai Lane,&nbsp;&nbsp; Stoke,<br><small>New Zealand.</small></div>

<svg class="abs" style="left:758px;top:64px" width="26" height="24" viewBox="0 0 26 24"><path d="M3 14a10 10 0 0 1 20 0" fill="none" stroke="#f47b0b" stroke-width="3"/><rect x="1" y="13" width="6" height="10" rx="2" fill="#f47b0b"/><rect x="19" y="13" width="6" height="10" rx="2" fill="#f47b0b"/></svg>
<div class="abs header-info" style="left:795px;top:62px">1800 - 555 - 0142/ EXT: 010<br><small>info@ridgelinebiketours.example</small></div>

<div class="abs logo"><span>RIDGELINE</span></div>

<svg class="abs navbar" width="1200" height="66" viewBox="0 0 1200 66">
  <rect x="0" y="0" width="1200" height="20" fill="#f47b0b"/>
  <path d="M300 0 H900 Q896 56 860 62 H345 Q310 56 300 0Z" fill="#f47b0b"/>
</svg>
<nav class="abs nav"><span>ABOUT US</span><span>WHAT WE OFFER</span><span>BOOKINGS/CONTACT</span></nav>

<!-- booking panel -->
<section class="abs book">
  <h3>BOOK NOW</h3>
  <div class="rule"></div>
  <div class="post">Type your Post code....</div>
  <div class="ret">&#9679;&nbsp; Return different location</div>
  <div class="dates">
    <div>
      <div class="lbl">PICK UP DATE &nbsp;&#9662;</div>
      <div class="day"><b>30</b><i>JULY<br>&nbsp;2018</i></div>
      <div class="time"><svg width="12" height="12" viewBox="0 0 12 12"><circle cx="6" cy="6" r="5" fill="none" stroke="#fff" stroke-width="1.5"/><path d="M6 3v3h2" stroke="#fff" fill="none"/></svg>01:00 AM</div>
    </div>
    <div>
      <div class="lbl">PICK UP DATE &nbsp;&#9662;</div>
      <div class="day"><b>20</b><i>JULY<br>&nbsp;2018</i></div>
      <div class="time"><svg width="12" height="12" viewBox="0 0 12 12"><circle cx="6" cy="6" r="5" fill="none" stroke="#fff" stroke-width="1.5"/><path d="M6 3v3h2" stroke="#fff" fill="none"/></svg>01:00 AM</div>
    </div>
  </div>
  <div class="btn">SUBMIT</div>
</section>

<!-- about -->
<h2 class="abs" style="left:173px;top:758px">ABOUT US</h2>
<div class="abs title-line" style="left:296px;top:767px;width:96px"></div>
<div class="abs" style="left:296px;top:773px;width:316px;height:1px;background:var(--orange)"></div>
<p class="abs about-copy">Lorem Ipsum is simply dummy text of the printing and typesetting industry. Lorem Ipsum has been the industry's standard dummy text ever since the 1500s, when an unknown printer took a galley of type and scrambled it to make a type specimen book. It has survived not only five centuries, but also the leap into electronic typesetting, remaining essentially unchanged. It was popularised in the 1960s with the release. Lorem Ipsum is simply dummy text of the printing and typesetting industry. Lorem Ipsum has been the industry's standard dummy text ever since the 1500s, when an unknown printer took a galley of type and scrambled it to make a type specimen book. It has survived not only five centuries, but also the leap into electronic typesetting, remaining essentially unchanged. It was popularised in the 1960s with the release.</p>
<div class="abs btn-dark">READ MORE</div>
<div class="abs video-frame"></div>
<div class="abs video-tag">VIDEO</div>
<div class="abs video-photo" role="img" aria-label="Video still of a mountain bike on a ridge overlooking the sea at sunset"><div class="abs play"></div></div>

<!-- what we offer -->
<div class="abs offer" role="img" aria-label="Dark forest trail background"></div>
<h2 class="abs white" style="left:0;top:1255px;width:1200px;text-align:center;font-size:30px">WHAT WE OFFER ?</h2>
<div class="abs title-line" style="left:580px;top:1304px;width:40px;height:2px"></div>
<p class="abs offer-lead">Lorem Ipsum has been the industry's standard dummy text ever since the 1500s, when an unknown printer took a galley of type and scrambled it to make a type specimen book. It has survived not only five centuries</p>

<div class="abs card" style="left:173px;top:1412px">
  <div class="ph" style="background:linear-gradient(180deg,#fff,#e9e9e9)" role="img" aria-label="Black electric mountain bike on white background"></div>
  <h4>BIKE RENTAL AND PRICING</h4>
  <p>Lorem Ipsum has been the industry's standard dummy text ever since the 1500s, when an unknown printer took a galley of type and scrambled it to make</p>
  <div class="btn">READ MORE</div>
</div>
<div class="abs card" style="left:466px;top:1412px">
  <div class="ph" style="background:linear-gradient(180deg,#8fb1cf 0%,#5d7f9e 40%,#6a6a3c 70%,#3a3522 100%)" role="img" aria-label="Orange mountain bike on a grassy hilltop with coastline behind"></div>
  <h4>GUIDED TOURS AND PRICING</h4>
  <p>Lorem Ipsum has been the industry's standard dummy text ever since the 1500s, when an unknown printer took a galley of type and scrambled it to make</p>
  <div class="btn">READ MORE</div>
</div>
<div class="abs card" style="left:757px;top:1412px">
  <div class="ph" style="background:linear-gradient(180deg,#fff,#e9e9e9)" role="img" aria-label="Grey and black electric mountain bike on white background"></div>
  <h4>RECOMMENDED PACKAGE DEALS</h4>
  <p>Lorem Ipsum has been the industry's standard dummy text ever since the 1500s, when an unknown printer took a galley of type and scrambled it to make</p>
  <div class="btn">READ MORE</div>
</div>

<!-- our video -->
<div class="abs videos"></div>
<h2 class="abs" style="left:173px;top:1838px">OUR VIDEO</h2>
<div class="abs title-line" style="left:308px;top:1851px;width:721px;height:3px"></div>
<div class="abs thumb" style="left:173px;top:1913px"><div class="ph" role="img" aria-label="Video still of forested hills under a cloudy sky"><div class="abs play"></div></div><p>LOREM IPSUM IS SIMPLY</p></div>
<div class="abs thumb" style="left:393px;top:1913px"><div class="ph" role="img" aria-label="Video still of forested hills under a cloudy sky"><div class="abs play"></div></div><p>LOREM IPSUM IS SIMPLY</p></div>
<div class="abs thumb" style="left:611px;top:1913px"><div class="ph" role="img" aria-label="Video still of forested hills under a cloudy sky"><div class="abs play"></div></div><p>LOREM IPSUM IS SIMPLY</p></div>
<div class="abs thumb" style="left:831px;top:1913px"><div class="ph" role="img" aria-label="Video still of forested hills under a cloudy sky"><div class="abs play"></div></div><p>LOREM IPSUM IS SIMPLY</p></div>
<svg class="abs arrow" style="left:162px;top:1970px" viewBox="0 0 27 27"><rect width="27" height="27" fill="#f47b0b"/><path d="M16 8l-6 5.5 6 5.5" stroke="#fff" stroke-width="2" fill="none"/></svg>
<svg class="abs arrow" style="left:1009px;top:1970px" viewBox="0 0 27 27"><rect width="27" height="27" fill="#f47b0b"/><path d="M11 8l6 5.5-6 5.5" stroke="#fff" stroke-width="2" fill="none"/></svg>

<!-- contact -->
<h2 class="abs" style="left:173px;top:2193px">CONTACT US</h2>
<div class="abs title-line" style="left:326px;top:2201px;width:96px;height:2px"></div>
<div class="abs" style="left:326px;top:2206px;width:312px;height:1px;background:var(--orange)"></div>
<div class="abs field" style="left:173px;top:2275px;width:270px">Type your name....</div>
<div class="abs field" style="left:466px;top:2275px;width:270px">Type your email....</div>
<div class="abs field" style="left:759px;top:2275px;width:270px">Type your phone no....</div>
<div class="abs field" style="left:173px;top:2321px;width:856px;height:110px">Type your message..</div>
<div class="abs btn" style="left:173px;top:2475px;width:129px;height:36px;line-height:36px">SUBMIT</div>

<!-- footer -->
<footer class="abs footer"></footer>
<div class="abs f-h" style="left:173px;top:2639px">ABOUT US</div>
<p class="abs f-txt" style="left:173px;top:2680px;width:292px">Lorem Ipsum is simply dummy text the printing and typesetting industry. Lorem Ipsum has been the industry's standard an unknown printer took a galley of type and scrambled it to make a type specimen book. been the industry's standard an unknown printer took a galley of type and scrambled it to make a type specimen book.</p>
<div class="abs f-h" style="left:516px;top:2639px">QUICK LINKS</div>
<ul class="abs f-list" style="left:516px;top:2687px"><li>About us</li><li>What We Offer</li><li>Bookings / Contact</li></ul>
<div class="abs f-h" style="left:663px;top:2639px">CONTACT INFO</div>
<div class="abs f-txt" style="left:663px;top:2685px;width:180px">
  <div style="display:flex;gap:8px"><svg width="10" height="14" viewBox="0 0 18 26"><path d="M9 0C4 0 0 4 0 9c0 7 9 17 9 17s9-10 9-17c0-5-4-9-9-9z" fill="#fff"/></svg><span>14 Kowhai Lane,<br>7011 Stoke, NZ</span></div>
  <div style="display:flex;gap:8px;margin-top:12px;align-items:center"><svg width="12" height="9" viewBox="0 0 12 9"><rect width="12" height="9" fill="#fff"/><path d="M0 0l6 5 6-5" stroke="#1f2137" fill="none"/></svg>hello@ridgelinetours.example</div>
  <div style="display:flex;gap:8px;margin-top:14px;align-items:center"><svg width="11" height="11" viewBox="0 0 12 12"><path d="M2 0l3 3-2 2c1 2 2 3 4 4l2-2 3 3-2 2C5 12 0 7 0 2z" fill="#fff"/></svg>+1800 - 555 - 0142/ EXT: 010</div>
</div>
<div class="abs f-h" style="left:880px;top:2639px">FOLLOW US</div>
<div class="abs social" style="left:880px;top:2688px"><span></span><span></span><span></span><span></span></div>
<div class="abs bottom">© 2018 Ridgeline E-Bike Tours NZ.All Rights Reserved.</div>

</body>
</html>
```